Einladungskarten-Design für Ehepaar
Zielgruppe
Wir sind ein Ehepaar und feiern 2 Geburtstage und eine Hochzeit in einem grossen Fest. Unsere Zielgruppe sind unsere Freunde.
Aufgabenstellung
Doppelkarte A5 quer, nur Frontseite designed; Briefing siehe Worddok

```html
<!DOCTYPE html>
<html lang="de">
<head>
<meta charset="utf-8">
<title>Einladung – 60x2</title>
<link rel="stylesheet" href="https://fonts.googleapis.com/css2?family=Archivo:wght@800&family=Montserrat:wght@300;700&family=Open+Sans:wght@300;400&family=Roboto+Condensed:wght@200&display=swap">
<style>
  :root {
    --sky-blue: #00aeef;
    --paper: #ffffff;
    --ink: #000000;
  }
  html, body {
    margin: 0;
    padding: 0;
    width: 1200px;
    height: 854px;
    overflow: hidden;
    background: var(--paper);
  }
  .invitation {
    position: relative;
    width: 1200px;
    height: 854px;
    background: var(--paper);
    overflow: hidden;
  }
  .invitation-word {
    position: absolute;
    left: 0;
    top: 0;
    width: 130px;
    height: 560px;
    margin: 0;
  }
  .invitation-word text {
    font-family: "Roboto Condensed", sans-serif;
    font-weight: 200;
    font-size: 97px;
    fill: var(--sky-blue);
  }
  .headline {
    position: absolute;
    left: 139px;
    top: 86px;
    margin: 0;
    font-family: "Archivo", sans-serif;
    font-weight: 800;
    font-size: 33px;
    line-height: 43.5px;
    letter-spacing: 1px;
    color: var(--sky-blue);
    text-transform: uppercase;
  }
  .headline span { display: block; white-space: nowrap; }
  .bubble {
    position: absolute;
    border-radius: 50%;
    background: var(--sky-blue);
    color: var(--paper);
    display: flex;
    align-items: center;
    justify-content: center;
    text-align: center;
  }
  .bubble--large { left: 769px; top: 31px; width: 380px; height: 380px; display: block; }
  .bubble--medium { left: 536px; top: 255px; width: 172px; height: 172px; }
  .bubble--small { left: 440px; top: 407px; width: 88px; height: 88px; }
  .bubble-figure--large {
    position: absolute;
    left: 0;
    right: 0;
    top: 115px;
    font-family: "Montserrat", sans-serif;
    font-weight: 700;
    font-size: 138px;
    line-height: 1;
    letter-spacing: -4px;
  }
  .bubble-figure--medium {
    font-family: "Montserrat", sans-serif;
    font-weight: 300;
    font-size: 66px;
    letter-spacing: -2px;
  }
  .bubble-figure--small {
    font-family: "Montserrat", sans-serif;
    font-weight: 300;
    font-size: 33px;
    letter-spacing: -1px;
  }
  .occasions {
    position: absolute;
    left: 98px;
    top: 296px;
    display: flex;
    align-items: center;
    gap: 8px;
    font-family: "Open Sans", sans-serif;
  }
  .occasion-list { text-align: left; position: relative; padding-left: 22px; }
  .occasion {
    display: block;
    font-size: 19px;
    line-height: 24px;
  }
  .occasion-count {
    position: absolute;
    left: 0;
    font-size: 38px;
    font-weight: 300;
    line-height: 1;
  }
  .occasion-count--two { top: -6px; }
  .occasion-count--one { top: 18px; left: 16px; }
  .occasion--second { padding-left: 14px; }
  .ampersand {
    font-size: 50px;
    font-weight: 300;
    margin-left: 6px;
  }
  .city-view {
    position: absolute;
    left: 0;
    top: 640px;
    width: 1200px;
    height: 214px;
    background: linear-gradient(180deg, #5ccbf4 0%, var(--sky-blue) 60%);
  }
  .profiles-motif {
    position: absolute;
    left: 92px;
    top: 518px;
    width: 392px;
    height: 336px;
    background: var(--ink);
    border-radius: 170px 170px 0 0;
  }
</style>
</head>
<body>
<main class="invitation">
  <h1 class="invitation-word">
    <svg width="130" height="560" viewBox="0 0 130 560" aria-label="EINLADUNG">
      <text transform="translate(110 531) rotate(-90)" x="0" y="0" textLength="503" lengthAdjust="spacingAndGlyphs">EINLADUNG</text>
    </svg>
  </h1>

  <p class="headline">
    <span>Dreifach Grund zu feiern</span>
    <span>Doppelter Geburtstag</span>
    <span>60 Jahre&nbsp; und eine Hochzeit</span>
    <span>Fest am 6.10.2018</span>
  </p>

  <div class="bubble bubble--large">
    <span class="bubble-figure--large">60x2</span>
    <div class="occasions">
      <div class="occasion-list">
        <span class="occasion-count occasion-count--two">2</span>
        <span class="occasion-count occasion-count--one">1</span>
        <span class="occasion">Geburtstage</span>
        <span class="occasion occasion--second">Hochzeit</span>
      </div>
      <span class="ampersand">&amp;</span>
    </div>
  </div>

  <div class="bubble bubble--medium">
    <span class="bubble-figure--medium">6x10</span>
  </div>

  <div class="bubble bubble--small">
    <span class="bubble-figure--small">6.10.</span>
  </div>

  <div class="city-view" role="img" aria-label="Blau eingefärbte Stadtansicht mit Kathedrale und Türmen"></div>
  <div class="profiles-motif" role="img" aria-label="Zwei einander zugewandte Kopfsilhouetten in Schwarz"></div>
</main>
</body>
</html>
```